Flyer-Design für Service-Plattform für Vor-Ort-Apotheken
Zielgruppe
Wir entwickeln eine Service-Plattform für Vor-Ort-Apotheken, über die Kunden bei Apotheken in der Umgebung online Medikamente kaufen und sich von den Apotheken über einen Livechat beraten lassen können.
Der Flyer soll ein Vertriebsflyer für die Apotheken werden.
Aufgabenstellung
Wir möchten, dass der Flyer vom Design her nicht zu formell wird, sondern möchten auch ein bisschen 'coolen Startup-Charakter' rüberbringen. Der Flyer soll ein zwei-Blatt-Flyer werden.
Ich werde noch einen ersten Entwurf anfügen, der uns leider nicht sehr angesprochen hat, da dieser einfach zu langweilig wirkte.
Die Roadmap im Flyer gefällt uns wirklich sehr gut, der Rest sollte mit Icons versehen werden und eventuell auch prägnante Worte sollten hervorgehoben werden.
Der Blauton ist auch der Ton, den wir auf unserer Website für Header und Footer verwenden, jedoch fehlte uns im ersten Entwurf des Flyers der Grünanteil (z.B. aus unserem Logo).
Falls es noch Fragen oder Anregungen gibt, bitte einfach melden :)!

```html
<!DOCTYPE html>
<html lang="de">
<head>
<meta charset="utf-8">
<title>Apotia – Serviceplattform Flyer</title>
<link href="https://fonts.googleapis.com/css2?family=Fira+Sans:wght@700;800&family=Source+Sans+3:wght@300;400;600;700&display=swap" rel="stylesheet">
<style>
  :root{
    --blue-dark:#1560c0;
    --blue:#1f72cf;
    --blue-light:#4fa6e8;
    --green:#6fbf3f;
    --grey:#7a7a7a;
    --white:#ffffff;
    --head:"Fira Sans", sans-serif;
    --body:"Source Sans 3", sans-serif;
  }
  *{margin:0;padding:0;box-sizing:border-box}
  html,body{width:1200px;height:846px;overflow:hidden;background:var(--white)}
  body{position:relative;font-family:var(--body)}
  .page{position:absolute;top:93px;width:318px;height:667px;background:var(--white);overflow:hidden}
  .page--front{left:247px}
  .page--back{left:677px}
  .page__shapes{position:absolute;inset:0;width:100%;height:100%}
  .abs{position:absolute}

  .brand{left:40px;top:38px;display:flex;align-items:center;gap:8px}
  .brand__name{font-family:var(--body);font-weight:300;font-size:26px;color:var(--white);letter-spacing:.5px}
  .brand__mark{width:20px;height:20px;background:var(--white);border-radius:3px}
  .brand__tagline{left:40px;top:68px;width:104px;height:13px;background:var(--green);color:var(--white);font-weight:600;font-size:10px;line-height:13px;text-align:center}

  .hero__kicker{left:40px;top:106px;font-weight:300;font-size:18px;color:var(--white)}
  .hero__title{left:40px;top:129px;font-family:var(--head);font-weight:800;font-size:17.5px;line-height:23.5px;color:var(--white);letter-spacing:.3px}
  .hero__text{left:40px;top:181px;width:212px;font-weight:300;font-size:10px;line-height:13.5px;color:var(--white)}
  .hero__text b,.benefit__text b,.cta__text b{font-weight:600}

  .section-title{font-family:var(--head);font-weight:800;font-size:17.5px;color:var(--green);letter-spacing:.3px}
  .section-sub{font-weight:300;font-size:18.5px;color:var(--green)}

  .step__num{font-family:var(--head);font-weight:800;font-size:31px;line-height:1}
  .step__num--1{color:var(--blue-dark)}
  .step__num--2{color:var(--blue)}
  .step__num--3{color:#2f8ae0}
  .step__num--4{color:var(--blue-light)}
  .step__label{font-size:8.6px;line-height:10.5px;color:var(--grey);letter-spacing:.8px;text-align:center;transform:translateX(-50%);white-space:nowrap}
  .icon-slot{border-radius:6px;background:linear-gradient(135deg,#d7e9fa,#b9d8f4)}

  .benefit__icon{left:40px;width:40px;height:36px}
  .benefit__title{left:90px;font-weight:600;font-size:12.5px;color:var(--blue);letter-spacing:.2px}
  .benefit__text{left:90px;width:188px;font-weight:300;font-size:10.5px;line-height:13.5px;color:var(--grey)}
  .benefit__text b{color:#555}

  .cta__title{left:40px;top:458px;font-family:var(--head);font-weight:800;font-size:17.5px;color:var(--white);letter-spacing:.3px}
  .cta__sub{left:40px;top:481px;font-weight:300;font-size:18.5px;color:var(--white)}
  .cta__text{left:40px;top:513px;width:236px;font-weight:300;font-size:10.5px;line-height:13.5px;color:var(--white)}
  .cta__rule{left:40px;top:568px;width:62px;height:1px;background:var(--white)}
  .cta__call{left:40px;top:581px;font-weight:600;font-size:12px;color:var(--white);letter-spacing:.2px}
  .cta__contact{left:40px;top:607px;font-weight:300;font-size:12px;line-height:16px;color:var(--white)}
  .cta__contact strong{font-weight:600}
</style>
</head>
<body>

<!-- Vorderseite -->
<section class="page page--front">
  <svg class="page__shapes" viewBox="0 0 603 1266" preserveAspectRatio="none" aria-hidden="true">
    <defs>
      <linearGradient id="blueFront" x1="0" y1="1" x2="1" y2="0">
        <stop offset="0" stop-color="#52a7e8"/>
        <stop offset="1" stop-color="#1560c0"/>
      </linearGradient>
    </defs>
    <path d="M520 15 L550 20 Q592 38 580 85 L462 555 Q440 612 388 592 L230 548 Z" fill="#6fbf3f"/>
    <path d="M0 0 L527 0 L551 470 Q555 536 490 540 L52 562 Q0 566 0 540 Z" fill="url(#blueFront)"/>
    <path d="M418 1170 Q448 1090 505 1105 L603 1160 L603 1266 L400 1266 Z" fill="#6fbf3f"/>
    <path d="M355 1210 Q352 1158 420 1155 L540 1152 Q575 1156 580 1200 L590 1266 L357 1266 Z" fill="url(#blueFront)"/>
    <g fill="none" stroke="#c8c8c8" stroke-width="4" stroke-dasharray="12 8" stroke-linecap="round">
      <path d="M225 812 Q100 812 66 858 Q45 900 76 940"/>
      <path d="M240 978 Q275 978 305 985"/>
      <path d="M385 1090 Q340 1126 260 1128"/>
    </g>
  </svg>

  <div class="abs brand"><span class="brand__name">Apotia</span><span class="brand__mark"></span></div>
  <div class="abs brand__tagline">Einfach gesund</div>

  <div class="abs hero__kicker">SERVICEPLATTFORM</div>
  <h1 class="abs hero__title">FÜR ERFOLGREICHE<br>APOTHEKEN</h1>
  <p class="abs hero__text">Apotia ist eine Serviceplattform um Ihre <b>lokale Apotheke</b> mit Kunden digital und persönlich zusammenzubringen. Neben einem <b>modernen Shopsystem</b> lässt sich durch umfangreiche Service- und Beratungsfunktionen die Persönlichkeit Ihrer Apotheke erleben.</p>

  <h2 class="abs section-title" style="left:40px;top:335px">KUNDENZUFRIEDENHEIT</h2>
  <div class="abs section-sub" style="left:40px;top:358px">IN 4 SCHRITTEN</div>

  <!-- Schritt 1 -->
  <div class="abs step__num step__num--1" style="left:124px;top:411px">1</div>
  <svg class="abs" style="left:145px;top:397px" width="42" height="42" viewBox="0 0 42 42" aria-label="Lupe">
    <circle cx="17" cy="17" r="14" fill="none" stroke="#1560c0" stroke-width="2.4"/>
    <circle cx="17" cy="17" r="10.5" fill="none" stroke="#4fa6e8" stroke-width="1.2"/>
    <path d="M27 27 L38 38" stroke="#1560c0" stroke-width="4" stroke-linecap="round"/>
  </svg>
  <div class="abs step__label" style="left:167px;top:446px">APOTHEKE<br>FINDEN</div>

  <!-- Schritt 2 -->
  <div class="abs step__num step__num--2" style="left:48px;top:485px">2</div>
  <div class="abs icon-slot" style="left:61px;top:458px;width:50px;height:42px" role="img" aria-label="Icon: Beraterin mit Sprechblase"></div>
  <div class="abs step__label" style="left:94px;top:505px">BERATEN<br>LASSEN</div>

  <!-- Schritt 3 -->
  <div class="abs step__num step__num--3" style="left:165px;top:506px">3</div>
  <div class="abs icon-slot" style="left:192px;top:495px;width:44px;height:40px" role="img" aria-label="Icon: Medikamentenpackung und Dose"></div>
  <div class="abs step__label" style="left:214px;top:542px">MEDIKAMENTE<br>BESTELLEN</div>

  <!-- Schritt 4 -->
  <div class="abs step__num step__num--4" style="left:64px;top:574px">4</div>
  <div class="abs icon-slot" style="left:90px;top:553px;width:38px;height:55px" role="img" aria-label="Icon: Hand hält Einkaufstasche"></div>
  <div class="abs step__label" style="left:111px;top:611px">BESTELLUNG<br>ABHOLEN</div>
</section>

<!-- Rückseite -->
<section class="page page--back">
  <svg class="page__shapes" viewBox="0 0 603 1266" preserveAspectRatio="none" aria-hidden="true">
    <defs>
      <linearGradient id="blueBack" x1="0" y1="1" x2="1" y2="0">
        <stop offset="0" stop-color="#52a7e8"/>
        <stop offset="1" stop-color="#1560c0"/>
      </linearGradient>
      <linearGradient id="blueCorner" x1="0" y1="1" x2="1" y2="0">
        <stop offset="0" stop-color="#55aaea"/>
        <stop offset="1" stop-color="#1f6fcb"/>
      </linearGradient>
    </defs>
    <path d="M603 88 L603 150 Q565 162 525 142 Z" fill="#6fbf3f"/>
    <path d="M360 0 L603 0 L603 90 Q545 148 470 150 Q440 148 420 115 Z" fill="url(#blueCorner)"/>
    <path d="M128 800 Q135 742 185 745 L500 815 L603 850 L603 1266 L128 1266 Z" fill="#6fbf3f"/>
    <path d="M0 825 L485 780 Q540 778 546 845 L588 1266 L0 1266 Z" fill="url(#blueBack)"/>
  </svg>

  <h2 class="abs section-title" style="left:40px;top:38px">IHRE VORTEILE</h2>
  <div class="abs section-sub" style="left:40px;top:61px">AUF EINEN BLICK</div>

  <div class="abs icon-slot benefit__icon" style="top:112px" role="img" aria-label="Icon: Handschlag"></div>
  <h3 class="abs benefit__title" style="top:108px">KUNDENBEZIEHUNG STÄRKEN</h3>
  <p class="abs benefit__text" style="top:126px">Im Fokus der Serviceplattform steht der Auf- und Ausbau einer <b>langfristigen Beziehung</b> zwischen Kunden und Apotheke</p>

  <div class="abs icon-slot benefit__icon" style="top:190px" role="img" aria-label="Icon: Auszeichnung mit Stern"></div>
  <h3 class="abs benefit__title" style="top:186px">WETTBEWERBSFÄHIGKEIT</h3>
  <p class="abs benefit__text" style="top:204px">Die Wettbewerbsposition gegenüber <b>digitalen Versandapotheken</b> wird gestärkt</p>

  <div class="abs icon-slot benefit__icon" style="top:255px" role="img" aria-label="Icon: Aufstieg zur Zielflagge"></div>
  <h3 class="abs benefit__title" style="top:251px">KUNDEN- &amp; UMSATZGEWINNUNG</h3>
  <p class="abs benefit__text" style="top:269px">Die digitale und mobile Kundenansprache erschließt <b>neue Zielgruppen</b> und steigert den <b>Umsatz im Tagesgeschäft</b></p>

  <div class="abs icon-slot benefit__icon" style="top:333px" role="img" aria-label="Icon: startende Rakete"></div>
  <h3 class="abs benefit__title" style="top:329px">GEMEINSAM IN DIE ZUKUNFT</h3>
  <p class="abs benefit__text" style="top:347px">Apotia begleitet die lokale Apotheke in eine <b>digitale Zukunft</b></p>

  <h2 class="abs cta__title">WACHSE GEMEINSAM</h2>
  <div class="abs cta__sub">MIT APOTIA</div>
  <p class="abs cta__text">Begleiten Sie uns beim Ausbau unserer Serviceplattform Apotia und nehmen Sie wesentlichen Einfluss auf die Richtung die wir gemeinsam einschlagen.</p>
  <div class="abs cta__rule"></div>
  <div class="abs cta__call">KONTAKTIEREN SIE UNS NOCH HEUTE!</div>
  <div class="abs cta__contact">0160 4827 3391 · info@apotia-plattform.de<br><strong>www.apotia-plattform.de</strong></div>
</section>

</body>
</html>
```